Gooey Breeze

I am creating an online slime shop that will sell handmade custom slimes. I need to be able to have payment/shipping options and the ability to change product photos since the product and product name will change often

Target Market(s)

Slime

Industry/Entity Type

Retail - online sales

Coding

Coded - Design and coding required

Number of Pages Required

2 page

Font styles to use
Sans Serif

Colors
0094D4
00A9DD
6FCCEA
C7EBF8
E9F6FB
E54698
E96AAD
F1A4CE
F9D9EA
FCEFF6
A7469A
B969AE
D3A5CF
EDDBEB
F8F0F9

Requirements
Must have
• My logo, my domain, ability to change photos of products for sale, payment options, shipping options, social media links, contact us,

```html
<!DOCTYPE html>
<html lang="en">
<head>
<meta charset="utf-8">
<title>Gooey Breeze — Handmade Slime Shop</title>
<link href="https://fonts.googleapis.com/css2?family=Montserrat:wght@600;700;800&family=Poppins:wght@400;500;600&display=swap" rel="stylesheet">
<style>
:root{
  --pink:#d1447f;
  --pink-bright:#e54698;
  --purple:#8a2bd0;
  --purple-deep:#7b22c4;
  --lavender:#e7d2f6;
  --teal:#9cdcdc;
  --grey:#e4e2e4;
  --grey-light:#f2f0f2;
  --ink:#2b2b2b;
  --text:#444;
  --white:#fff;
}
*{box-sizing:border-box;margin:0;padding:0}
html,body{width:1200px;height:4922px;overflow:hidden}
body{font-family:'Poppins',sans-serif;color:var(--text);background:var(--white);position:relative}
.abs{position:absolute}
section,header,nav,footer{position:absolute;left:0;width:1200px}
.btn-grad{position:absolute;display:flex;align-items:center;justify-content:center;background:linear-gradient(90deg,var(--purple),var(--pink-bright));color:#fff;font-family:'Montserrat',sans-serif;font-weight:700;font-size:15px;letter-spacing:.3px}
.section-title{position:absolute;left:0;width:1200px;text-align:center;font-family:'Montserrat',sans-serif;font-weight:800;font-size:37px;color:var(--purple);letter-spacing:.5px}
.section-lead{position:absolute;left:200px;width:800px;text-align:center;font-size:14.5px;line-height:30px;color:#444}

/* top bar */
.topbar{top:0;height:54px;left:287px;width:913px;background:var(--pink);clip-path:polygon(26px 0,100% 0,100% 100%,0 100%)}
.topbar-item{position:absolute;top:0;height:54px;display:flex;align-items:center;gap:12px;color:#fff;font-size:15px}
.topbar-icon{width:30px;height:30px;border-radius:50%;background:rgba(255,255,255,.25);display:flex;align-items:center;justify-content:center}
.header{top:0;height:151px}
.brand{position:absolute;left:40px;top:48px;display:flex;align-items:center;gap:10px;font-family:'Poppins',sans-serif;font-weight:600;font-size:26px;color:var(--pink-bright)}
.brand-dot{width:22px;height:22px;border-radius:50%;background:var(--ink)}
.search{position:absolute;left:296px;top:82px;width:331px;height:46px;border:1px solid #ddd;box-shadow:0 2px 6px rgba(0,0,0,.12);display:flex;align-items:center;padding:0 16px;font-size:13px;color:#777;justify-content:space-between}
.header-link{position:absolute;top:86px;display:flex;align-items:center;gap:12px;font-size:16px;color:#333}
.header-icon{width:34px;height:34px;border-radius:50%;border:1px solid #ddd;display:flex;align-items:center;justify-content:center}

/* nav */
.nav{top:151px;height:55px;background:var(--purple)}
.nav a{position:absolute;top:0;height:55px;line-height:55px;color:#fff;font-size:15.5px;text-decoration:none}
.nav a.active::before{content:"";position:absolute;left:-8px;right:-8px;top:0;height:4px;background:#cfe9ff;border-radius:2px}

/* hero */
.hero{top:206px;height:625px}
.hero-photo{position:absolute;inset:0;background:linear-gradient(90deg,#c9498d 0%,#c45c95 32%,#b79aa8 52%,#9fa7b0 72%,#7f8e9a 100%)}
.hero-kicker{position:absolute;left:110px;top:150px;font-family:'Montserrat',sans-serif;font-weight:800;font-size:33px;color:#fff}
.hero-title{position:absolute;left:108px;top:200px;font-family:'Montserrat',sans-serif;font-weight:800;font-size:50px;color:#fff;letter-spacing:.5px}
.hero-text{position:absolute;left:110px;top:275px;width:520px;font-size:14.5px;line-height:31px;color:#fff}
.hero-btn{position:absolute;left:128px;top:365px;width:161px;height:43px;background:#fff;color:#111;font-family:'Montserrat',sans-serif;font-weight:700;font-size:16px;display:flex;align-items:center;justify-content:center}

/* about */
.about{top:831px;height:386px;background:var(--grey)}

/* products */
.products{top:1217px;height:1607px}
.product-card{position:absolute;width:503px;height:590px;border:12px solid var(--lavender);background:#fff}
.product-img{position:absolute;left:0;top:0;width:479px;height:432px}
.product-foot{position:absolute;left:0;top:432px;width:479px;height:134px;border-top:1px solid #e6e6e6}
.product-foot p{position:absolute;left:24px;top:44px;width:240px;font-size:14.5px;line-height:23px;color:#222}
.product-foot .add{position:absolute;left:323px;top:58px;width:139px;height:38px;font-size:14px}
.product-foot.hot{background:var(--purple-deep)}
.product-foot.hot p{color:#fff}
.product-foot.hot .add{background:#fff;color:var(--purple)}

/* brand history */
.history{top:2824px;height:428px;background:var(--teal)}
.history-brand{position:absolute;left:150px;top:190px;display:flex;align-items:center;gap:14px;font-weight:600;font-size:44px;color:var(--pink-bright)}
.history-brand .brand-dot{width:36px;height:36px}
.history-title{position:absolute;left:630px;top:86px;font-family:'Montserrat',sans-serif;font-weight:800;font-size:37px;color:var(--pink)}
.history-text{position:absolute;left:632px;top:145px;width:465px;font-size:14.5px;line-height:31px;color:#333}

/* upcoming */
.upcoming{top:3252px;height:774px}
.arrow{position:absolute;top:431px;width:34px;height:34px;border-radius:50%;background:var(--purple);display:flex;align-items:center;justify-content:center}
.up-card{position:absolute;top:222px;width:304px;height:460px}
.up-img{position:absolute;left:0;top:0;width:304px;height:329px}
.up-info{position:absolute;left:10px;top:316px;width:284px;height:147px;background:#fff;box-shadow:0 4px 10px rgba(0,0,0,.12);text-align:center}
.up-price{margin-top:14px;font-size:20px;color:#999}
.up-name{font-family:'Montserrat',sans-serif;font-weight:700;font-size:17px;color:#111;margin-top:2px}
.up-sub{font-size:16px;color:#aaa;margin-top:2px}
.up-btn{position:absolute;left:42px;top:129px;width:220px;height:46px;background:#fff;border:2px solid #222;box-shadow:3px 4px 8px rgba(0,0,0,.25);font-family:'Montserrat',sans-serif;font-weight:700;font-size:16px;color:#111;display:flex;align-items:center;justify-content:center}
.up-card.hot .up-info{background:var(--purple-deep)}
.up-card.hot .up-price,.up-card.hot .up-name,.up-card.hot .up-sub{color:#fff}
.up-card.hot .up-btn{background:var(--purple-deep);color:#fff;border-color:#fff}

/* newsletter */
.newsletter{top:4026px;height:341px;background:var(--grey-light)}
.news-form{position:absolute;left:243px;top:212px;width:712px;height:62px;display:flex}
.news-input{width:481px;height:62px;border:1px solid var(--purple);background:#fff;padding-left:32px;display:flex;align-items:center;font-size:14px;color:#555}
.news-btn{width:231px;height:62px;background:var(--purple-deep);color:#fff;font-family:'Montserrat',sans-serif;font-weight:700;font-size:18px;display:flex;align-items:center;justify-content:center}

/* features */
.features{top:4367px;height:181px;background:#fff}
.feature{position:absolute;top:68px;display:flex;align-items:center;gap:18px}
.feature-icon{width:52px;height:52px;border-radius:50%;background:#f3eef0;display:flex;align-items:center;justify-content:center}
.feature h4{font-family:'Poppins',sans-serif;font-weight:500;font-size:19px;color:#222}
.feature p{font-size:15px;color:#555}

/* footer */
.footer{top:4548px;height:374px;background:var(--pink);color:#fff}
.footer-brand{position:absolute;left:140px;top:155px;display:flex;align-items:center;gap:10px;font-weight:600;font-size:28px;color:#fff}
.footer-brand .brand-dot{background:#fff}
.footer-col{position:absolute;top:64px}
.footer-col h5{font-family:'Montserrat',sans-serif;font-weight:700;font-size:19px;margin-bottom:12px}
.footer-col li{list-style:none;font-size:13.5px;line-height:31px}
.footer-rule{position:absolute;left:111px;top:315px;width:978px;height:1px;background:rgba(255,255,255,.5)}
.copyright{position:absolute;left:0;top:334px;width:1200px;text-align:center;font-size:15px}
</style>
</head>
<body>

<header class="header">
  <div class="brand"><span class="brand-dot"></span>Gooey Breeze</div>
  <div class="search">Search Here
    <svg width="18" height="18" viewBox="0 0 24 24" fill="none" stroke="#333" stroke-width="2.5"><circle cx="10" cy="10" r="7"/><line x1="15" y1="15" x2="21" y2="21"/></svg>
  </div>
  <div class="header-link" style="left:680px"><span class="header-icon"><svg width="16" height="16" viewBox="0 0 24 24" fill="var(--pink-bright)"><circle cx="12" cy="8" r="5"/><path d="M3 22c0-5 4-8 9-8s9 3 9 8z"/></svg></span>Account</div>
  <div class="header-link" style="left:856px;top:84px"><span class="header-icon"><svg width="16" height="16" viewBox="0 0 24 24" fill="var(--pink-bright)"><path d="M2 3h3l3 12h11l3-9H7"/><circle cx="9" cy="20" r="2"/><circle cx="18" cy="20" r="2"/></svg></span>Cart</div>
  <div class="header-link" style="left:1003px"><span class="header-icon"><svg width="16" height="16" viewBox="0 0 24 24" fill="var(--pink-bright)"><circle cx="12" cy="8" r="5"/><path d="M3 22c0-5 4-8 9-8s9 3 9 8z"/></svg></span>Login</div>
</header>

<div class="topbar abs">
  <div class="topbar-item" style="left:15px"><span class="topbar-icon"><svg width="16" height="16" viewBox="0 0 24 24" fill="#fff"><path d="M1 5h13v10H1zM14 9h5l3 3v3h-8z"/><circle cx="6" cy="18" r="2"/><circle cx="17" cy="18" r="2"/></svg></span>Free shipping from $ 700</div>
  <div class="topbar-item" style="left:309px"><span class="topbar-icon"><svg width="14" height="14" viewBox="0 0 24 24" fill="#fff"><path d="M6 2l4 5-2 3c1 3 3 5 6 6l3-2 5 4-3 4C10 22 2 14 2 5z"/></svg></span>555 - 214 - 0937</div>
  <div class="topbar-item" style="left:542px"><span class="topbar-icon"><svg width="15" height="15" viewBox="0 0 24 24" fill="#fff"><path d="M2 5h20v14H2z"/><path d="M2 5l10 8 10-8" stroke="#d1447f" stroke-width="2" fill="none"/></svg></span>hello@gooeybreeze.shop</div>
</div>

<nav class="nav">
  <a class="active" style="left:115px">HOME</a>
  <a style="left:222px">ABOUT US</a>
  <a style="left:359px">OUR PRODUCTS</a>
  <a style="left:545px">UPCOMING PRODUCTS</a>
  <a style="left:781px">CART / ACCOUNT</a>
  <a style="left:982px">CONTACT US</a>
</nav>

<section class="hero">
  <div class="hero-photo" role="img" aria-label="Child playing with stretchy blue slime at a table, with a pink tint on the left"></div>
  <div class="hero-kicker">WELCOME TO</div>
  <div class="hero-title">GOOEY BREEZE</div>
  <p class="hero-text">Lorem ipsum dolor sit amet, consectetur adipiscing elit, sed do eiusmod tempor incididunt ut labore et dolore magna aliqua.</p>
  <div class="hero-btn">ORDER NOW</div>
</section>

<section class="about">
  <h2 class="section-title" style="top:58px">ABOUT&nbsp; GOOEY BREEZE</h2>
  <p class="section-lead" style="top:123px">Lorem ipsum dolor sit amet, consectetur adipiscing elit, sed do eiusmod tempor incididunt ut labore et dolore magna aliqua. Ut enim ad minim veniam, quis nostrud exercitation ullamco laboris nisi ut aliquip ex ea commodo consequat. Duis aute irure dolor in reprehenderit in voluptate velit esse cillum dolore eu fugiat nulla pariatur. Excepteur sint occaecat cupidatat non proident,</p>
  <div class="btn-grad" style="left:520px;top:277px;width:160px;height:42px">READ MORE</div>
</section>

<section class="products">
  <h2 class="section-title" style="top:60px">OUR PRODUCTS</h2>
  <p class="section-lead" style="top:125px">Lorem ipsum dolor sit amet, consectetur adipiscing elit, sed do eiusmod tempor incididunt ut labore et dolore magna aliqua. Ut enim ad minim veniam.</p>

  <div class="product-card" style="left:78px;top:220px">
    <div class="product-img" role="img" aria-label="Jar of pink and pastel slime topped with two small cat figures" style="background:linear-gradient(180deg,#e9a4b6,#e34c88 40%,#d9c890 70%,#8ab9d4)"></div>
    <div class="product-foot"><p>Lorem ipsum dolor sit amet, consectetur adipiscing elit, sed do eiusmod .</p><div class="btn-grad add">ADD TO CART</div></div>
  </div>
  <div class="product-card" style="left:617px;top:220px">
    <div class="product-img" role="img" aria-label="Jar of pink slime topped with a waffle-shaped sprinkle decoration" style="background:linear-gradient(180deg,#8a8680,#e8c2c6 40%,#d896b6 70%,#c875c4)"></div>
    <div class="product-foot"><p>Lorem ipsum dolor sit amet, consectetur adipiscing elit, sed do eiusmod .</p><div class="btn-grad add">ADD TO CART</div></div>
  </div>
  <div class="product-card" style="left:78px;top:870px">
    <div class="product-img" role="img" aria-label="Spread of glossy dark blue slime with beads and a small toy duck" style="background:radial-gradient(ellipse at center,#2a8fb5,#145f86 60%,#ffffff 75%)"></div>
    <div class="product-foot hot"><p>Lorem ipsum dolor sit amet, consectetur adipiscing elit, sed do eiusmod .</p><div class="btn-grad add">ADD TO CART</div></div>
  </div>
  <div class="product-card" style="left:617px;top:870px">
    <div class="product-img" role="img" aria-label="Spread of bright blue slime decorated with frogs, lily pads and flowers" style="background:radial-gradient(ellipse at center,#43bde0,#2aa6d4 55%,#ffffff 72%)"></div>
    <div class="product-foot" style="top:432px"><p style="top:56px">Lorem ipsum dolor sit amet, consectetur adipiscing elit, sed do eiusmod .</p><div class="btn-grad add" style="top:70px">ADD TO CART</div></div>
  </div>

  <div class="btn-grad" style="left:480px;top:1514px;width:239px;height:42px">VIEW MORE PRODUCTS</div>
</section>

<section class="history">
  <div class="history-brand"><span class="brand-dot"></span>Gooey Breeze</div>
  <h2 class="history-title">BRAND HISTORY</h2>
  <p class="history-text">Lorem ipsum dolor sit amet, consectetur adipiscing elit, sed do eiusmod tempor incididunt ut labore et dolore magna aliqua. Ut enim ad minim veniam, quis nostrud exercitation ullamco laboris nisi ut aliquip ex ea commodo consequat.</p>
  <div class="btn-grad" style="left:632px;top:289px;width:161px;height:42px">ORDER NOW</div>
</section>

<section class="upcoming">
  <h2 class="section-title" style="top:63px">UPCOMING PRODUCTS</h2>
  <p class="section-lead" style="top:124px">Lorem ipsum dolor sit amet, consectetur adipiscing elit, sed do eiusmod tempor incididunt ut labore et dolore magna aliqua. Ut enim ad minim veniam.</p>

  <div class="arrow" style="left:25px"><svg width="18" height="14" viewBox="0 0 18 14" fill="none" stroke="#fff" stroke-width="2"><path d="M17 7H2M7 1L1 7l6 6"/></svg></div>
  <div class="arrow" style="left:1139px"><svg width="18" height="14" viewBox="0 0 18 14" fill="none" stroke="#fff" stroke-width="2"><path d="M1 7h15M11 1l6 6-6 6"/></svg></div>

  <div class="up-card" style="left:111px">
    <div class="up-img" role="img" aria-label="Hands squeezing lilac glitter slime" style="background:linear-gradient(180deg,#eceaf4,#cdbbe3 60%,#e8d6cc)"></div>
    <div class="up-info"><div class="up-price">$232.33</div><div class="up-name">Lorem ipsum dolor</div><div class="up-sub">Lorem ipsum dolor sit amet</div><div class="up-btn">Add to Cart</div></div>
  </div>
  <div class="up-card hot" style="left:449px">
    <div class="up-img" role="img" aria-label="Hand holding pastel unicorn-themed slime" style="background:linear-gradient(180deg,#b08ac9,#d7a6d4 50%,#efc6d9)"></div>
    <div class="up-info"><div class="up-price">$232.33</div><div class="up-name">Lorem ipsum dolor</div><div class="up-sub">Lorem ipsum dolor sit amet</div><div class="up-btn">Add to Cart</div></div>
  </div>
  <div class="up-card" style="left:785px">
    <div class="up-img" role="img" aria-label="Splash of lime green slime" style="background:linear-gradient(180deg,#ffffff,#e8f3d8 35%,#9ccc3f 75%,#86b832)"></div>
    <div class="up-info"><div class="up-price">$232.33</div><div class="up-name">Lorem ipsum dolor</div><div class="up-sub">Lorem ipsum dolor sit amet</div><div class="up-btn">Add to Cart</div></div>
  </div>
</section>

<section class="newsletter">
  <h2 class="section-title" style="top:60px">SUBSCRIBE TO OUR NEWSLETTER</h2>
  <p class="section-lead" style="top:125px">Lorem ipsum dolor sit amet, consectetur adipiscing elit, sed do eiusmod tempor incididunt ut labore et dolore magna aliqua. Ut enim ad minim veniam.</p>
  <div class="news-form"><div class="news-input">Enter Your Mail</div><div class="news-btn">SUBSCRIBE</div></div>
</section>

<section class="features">
  <div class="feature" style="left:119px">
    <span class="feature-icon"><svg width="30" height="30" viewBox="0 0 24 24" fill="none" stroke="#555" stroke-width="1.4"><rect x="3" y="9" width="18" height="12"/><rect x="2" y="6" width="20" height="4"/><path d="M12 6v15M12 6c-2-4-6-4-5-1M12 6c2-4 6-4 5-1"/></svg></span>
    <div><h4>Gift Wrap</h4><p>Lorem ipsum dolor sit amet.</p></div>
  </div>
  <div class="feature" style="left:496px">
    <span class="feature-icon"><svg width="30" height="30" viewBox="0 0 24 24" fill="none" stroke="#555" stroke-width="1.4"><path d="M1 6h13v10H1zM14 10h5l3 3v3h-8z"/><circle cx="6" cy="18" r="2"/><circle cx="17" cy="18" r="2"/></svg></span>
    <div><h4>Free Delivery</h4><p>Lorem ipsum dolor sit amet.</p></div>
  </div>
  <div class="feature" style="left:826px">
    <span class="feature-icon"><svg width="30" height="30" viewBox="0 0 24 24" fill="none" stroke="#555" stroke-width="1.4"><path d="M4 14v-2a8 8 0 0 1 16 0v2"/><rect x="3" y="13" width="4" height="6" rx="1"/><rect x="17" y="13" width="4" height="6" rx="1"/><path d="M19 19c0 2-3 3-6 3"/></svg></span>
    <div><h4>support</h4><p>Lorem ipsum dolor sit amet.</p></div>
  </div>
</section>

<footer class="footer">
  <div class="footer-brand"><span class="brand-dot"></span>Gooey Breeze</div>
  <div class="footer-col" style="left:443px"><h5>QUICK LINKS</h5><ul><li>Home</li><li>About Us</li><li>Our Products</li><li>Upcoming Products</li><li>Cart / Account</li><li>Contact Us</li></ul></div>
  <div class="footer-col" style="left:673px"><h5>USEFUL LINKS</h5><ul><li>Privacy</li><li>Terms of Use</li><li>Cookie preferences</li><li>information</li><li>Site Map</li><li>Contact</li></ul></div>
  <div class="footer-col" style="left:896px"><h5>OUR PRODUCTS</h5><ul><li>Lorem ipsum dolor</li><li>Lorem ipsum dolor</li><li>Lorem ipsum dolor</li><li>Lorem ipsum dolor</li><li>Lorem ipsum dolor</li><li>Lorem ipsum dolor</li></ul></div>
  <div class="footer-rule"></div>
  <div class="copyright">© 2024 Gooey Breeze. All Rights Reserved</div>
</footer>

</body>
</html>
```